In house, web site post, social media post, and email blast specials/promo flyer

We are looking to update our monthly specials flyer to be sent out via Bright Mailway as well as printed and handed out in office and social media and posted to our website. Please see attachments below for a sample of a previous flyer. We want it to look clean and not too busy. It should be professional looking as this is going to a higher end client that is paying cash for our services

Target Market(s)

Women and Men 35-55

Contact Information for Business Card

I am tired of our current business card and want a fresh updated look. We want something simple, clean, and modern looking.

Font styles to use
Sans Serif
Script

Colors
3377b5
34a7d8
85cae6
85abd2
cedeed
ecf7fb
eaf1f7

Requirements
Must have
• Clean lines, Sexy, appealing to the medical spa beauty industry. Our clients come to us to look and feel good.
• Content of actual specials:
• FIGHT FINE LINES AND WRINKLES-Purchase a minimum of 30 units of Lumivex and receive a complimentary Glycolic Acid Peel ($150 VALUE)
• THE SWEAT STOPS HERE-Permanently stop underarm sweat with DuraCalm treatments, starting at $1,950
• BRIGHTEN & TONE-IPL $ Beam Serenity package $3,500
• REDUCE FACE & LEG VEINS- 15% off packages
• VOLUMERA: CHEEKS & NL FOLDS-SECOND SYRINGE 25% OFF, THIRD SYRINGE $50 OFF
• BODY SCULPTING FOR ABDOMEN AND THIGHS-Blast unwanted fat with a trio of treatments! $4,799
Nice to have
• Here are some sample flyers of what we would like ours to look like
• https://www.kelomirskinspa.com/specials/
• https://brevanolaclinic.com/november-specials-2017/

```html
<!DOCTYPE html>
<html lang="en">
<head>
<meta charset="utf-8">
<title>Lumara Monthly Specials</title>
<link rel="stylesheet" href="https://fonts.googleapis.com/css2?family=Lato:wght@400;700&family=Lobster&family=Roboto+Condensed:ital@1&family=Libre+Baskerville:wght@700&display=swap">
<style>
  :root {
    --ink-teal: #1e4d58;
    --brand-teal: #2a5a63;
    --banner-dark: #2e6470;
    --banner-light: #7fb0b8;
    --olive: #a89a35;
    --price-red: #e8282e;
    --tag-grey: #e6e6e6;
    --accent-blue: #2f6ea8;
    --value-teal: #2d6d78;
    --body-ink: #2b2b2b;
    --stage: #e9eef0;
  }
  * { margin: 0; padding: 0; box-sizing: border-box; }
  html, body { width: 1200px; height: 1200px; overflow: hidden; background: var(--stage); }
  .canvas { position: relative; width: 1200px; height: 1200px; }
  .flyer {
    position: absolute; left: 136px; top: 0;
    width: 842px; height: 1089px;
    transform: scale(1.102); transform-origin: 0 0;
    background: #fff; overflow: hidden;
    font-family: "Lato", sans-serif; color: var(--body-ink);
  }
  .abs { position: absolute; }
  .side-panel {
    left: 405px; top: 318px; width: 437px; height: 719px;
    background: linear-gradient(180deg, #f2f7f8 0%, #c9dfe3 35%, #5b96a1 100%);
  }
  .banner {
    left: 0; top: 248px; width: 490px; height: 70px;
    background: linear-gradient(90deg, var(--banner-dark) 0%, var(--banner-light) 100%);
  }
  .banner-title {
    left: 0; top: 248px; width: 410px; height: 70px; line-height: 70px; text-align: center;
    font-family: "Lobster", cursive; font-size: 44px; color: #fff;
  }
  .hero-photo { left: 0; top: 0; width: 842px; height: 640px; }
  .brand { left: 48px; top: 92px; }
  .brand-name { font-family: "Lato", sans-serif; font-weight: 400; font-size: 74px; letter-spacing: 2px; color: var(--brand-teal); line-height: 1; }
  .brand-tagline { margin: 8px 0 0 152px; font-family: "Roboto Condensed", sans-serif; font-style: italic; font-size: 26px; color: var(--brand-teal); }
  .special { left: 38px; width: 346px; }
  .special h3 { font-size: 16px; font-weight: 700; color: var(--ink-teal); line-height: 20px; }
  .special p { font-size: 15px; line-height: 20px; text-align: justify; }
  .price-tag {
    position: absolute; left: 112px; width: 162px; height: 52px; background: var(--tag-grey);
    padding: 7px;
  }
  .price-tag span {
    display: block; height: 100%; border: 1.5px dashed var(--price-red);
    color: var(--price-red); font-size: 19px; font-weight: 700; text-align: center; line-height: 35px;
  }
  .syringe-row { display: flex; font-size: 16px; line-height: 28px; font-weight: 700; color: var(--body-ink); }
  .syringe-row b { width: 170px; }
  .syringe-row em { font-style: normal; font-size: 19px; color: var(--value-teal); font-weight: 400; }
  .accent { color: var(--accent-blue); }
  .veins-offer {
    left: 459px; top: 651px; width: 289px; height: 116px; background: var(--tag-grey);
    padding: 9px 12px; box-shadow: 0 14px 14px -10px rgba(0,0,0,0.35);
  }
  .veins-offer div {
    height: 100%; border: 1.5px dashed var(--price-red); text-align: center; padding-top: 9px;
  }
  .veins-offer h4 { font-size: 17px; font-weight: 700; color: var(--ink-teal); }
  .veins-offer strong { display: block; font-family: "Libre Baskerville", serif; font-size: 33px; color: var(--price-red); line-height: 40px; }
  .veins-offer small { font-size: 15px; color: #333; }
  .spa-still { left: 420px; top: 790px; width: 330px; height: 290px; }
  .footer-band { left: 0; top: 1037px; width: 842px; height: 52px; background: var(--olive); }
  .site-url {
    left: 0; top: 1037px; width: 540px; height: 52px; line-height: 52px; text-align: center;
    color: #fff; font-size: 17px; letter-spacing: 4px;
  }
</style>
</head>
<body>
<main class="canvas">
  <article class="flyer">
    <div class="abs side-panel"></div>
    <div class="abs banner"></div>
    <h2 class="abs banner-title">Actual Specials</h2>

    <svg class="abs hero-photo" viewBox="0 0 842 640" role="img" aria-label="Photo of a smiling woman in a straw sun hat against a bright summer field">
      <defs>
        <linearGradient id="heroTone" x1="0" y1="0" x2="0" y2="1">
          <stop offset="0" stop-color="#f6f0e4"/>
          <stop offset="0.45" stop-color="#e9d2c2"/>
          <stop offset="0.7" stop-color="#d9b9d8"/>
          <stop offset="1" stop-color="#e6c6e6"/>
        </linearGradient>
      </defs>
      <path d="M300,0 L842,0 L842,620 L470,620 C440,400 380,150 300,0 Z" fill="url(#heroTone)"/>
    </svg>

    <header class="abs brand">
      <h1 class="brand-name">LUMARA</h1>
      <p class="brand-tagline">Age Beautifully</p>
    </header>

    <section class="abs special" style="top:337px">
      <h3>FIGHT FINE LINES AND WRINKLES-</h3>
      <p>Purchase a minimum of 30 units of Lumivex and receive a complimentary Glycolic Acid Peel</p>
    </section>
    <div class="price-tag" style="top:418px"><span>($150 VALUE)</span></div>

    <section class="abs special" style="top:507px">
      <h3>THE SWEAT STOPS HERE-</h3>
      <p>Permanently stop underarm sweat with DuraCalm treatments, starting at</p>
    </section>
    <div class="price-tag" style="top:582px"><span>$1,950</span></div>

    <section class="abs special" style="top:662px">
      <h3>BRIGHTEN &amp; TONE-</h3>
      <p>IPL $ Beam Serenity package</p>
    </section>
    <div class="price-tag" style="top:708px"><span>$3,500</span></div>

    <section class="abs special" style="top:789px">
      <h3><span class="accent">VOLUMERA</span>: CHEEKS &amp; NL FOLDS-</h3>
      <div class="syringe-row" style="margin-top:6px"><b>SECOND SYRINGE</b><em>25% OFF</em></div>
      <div class="syringe-row"><b>THIRD SYRINGE</b><em>$50 OFF</em></div>
    </section>

    <section class="abs special" style="top:905px">
      <h3>BODY SCULPTING FOR ABDOMEN AND THIGHS-</h3>
      <p style="margin-top:2px">Blast unwanted fat with a trio of treatments!</p>
    </section>
    <div class="price-tag" style="top:975px"><span>$4,799</span></div>

    <aside class="abs veins-offer">
      <div>
        <h4>REDUCE FACE &amp; LEG VEINS-</h4>
        <strong>15% OFF</strong>
        <small>PACKAGES</small>
      </div>
    </aside>

    <svg class="abs spa-still" viewBox="0 0 330 290" role="img" aria-label="Photo of stacked spa stones with pink frangipani flowers and green leaves">
      <defs>
        <radialGradient id="stoneTone" cx="0.5" cy="0.55" r="0.55">
          <stop offset="0" stop-color="#5b5a4e"/>
          <stop offset="0.7" stop-color="#3a3a33"/>
          <stop offset="1" stop-color="#3a3a33" stop-opacity="0"/>
        </radialGradient>
      </defs>
      <ellipse cx="170" cy="150" rx="150" ry="140" fill="url(#stoneTone)"/>
    </svg>

    <footer>
      <div class="abs footer-band"></div>
      <p class="abs site-url">www.lumaraportland.com</p>
    </footer>
  </article>
</main>
</body>
</html>
```